BRISK is looking for a design partner

We are a group of videographers, photographers and editors currently rebranding our company. Originally Marco Lenhill Photography, we have grown over the years into a company that does a lot of different things for a variety of corporate clients. It's clear the company is no longer Marco, but a whole team. We have submitted a design contest for our new logo, purchased our new URL/email, and are now looking to get things moving on the website. We have most copy ready and are looking to help move online. The site should load quickly, be mobile friendly, look modern, and be very easy to navigate. Our videos run on Flickcast so we need to make sure that we can embed or run videos from the Flickcast account.

We are excited to be starting this new chapter. Hopefully you can come along with us! Marco

Target Market(s)

Businesses looking to see what we do, examples of our work, and who we are.

Industry/Entity Type

Multimedia

Font styles to use
Serif
Sans Serif

Colors
33a6d7
3176b5
ffffff

Requirements
Must have
• I believe we are looking for a bright white background website.

Here is a list of areas that we will need to have on the site.
-Overview video near top
-Our Mission
-Details of services
-About the team
-Our History (3 sections: Different from Start, Growth, Transformation)
-Working at BRISK (area for talent and freelancer to see employment info, current opening, how to apply
-Internship Program details
-Contact Form
-FAQ
Nice to have
• Social media links, slideshow, etc
We need photo and videos sprinkled throughout the site to give it as modern a look as possible. I am open to using this for backgrounds or to segment sections. See our current site here marcolenhillphotography.example/business/
Should not have
• Cannot load slow. This is our current challenge. Any thing we can do to move this along will be helpful.

```html
<!DOCTYPE html>
<html lang="en">
<head>
<meta charset="utf-8">
<title>BRISK — Home</title>
<link href="https://fonts.googleapis.com/css2?family=Open+Sans:wght@300;400;600&family=Ubuntu+Condensed&family=Roboto+Condensed:wght@300;400&family=Ubuntu:wght@300;400&display=swap" rel="stylesheet">
<style>
:root{
  --blue:#33a6d7;
  --blue-deep:#0792cf;
  --blue-head:#1b8fd1;
  --ink:#222;
  --text:#666;
  --stage:#e3e3e3;
  --soft:#f4f4f4;
  --white:#fff;
  --cond:"Ubuntu Condensed","Roboto Condensed","Arial Narrow",sans-serif;
}
*{margin:0;padding:0;box-sizing:border-box}
html,body{width:1200px;height:2581px;overflow:hidden}
body{background:var(--stage);font-family:"Open Sans",sans-serif;color:var(--text)}
.page{position:absolute;left:99px;top:0;width:1002px;height:2581px;background:var(--white);overflow:hidden}
.photo{position:absolute}
.cond{font-family:var(--cond);font-stretch:condensed}
/* header */
.nav{position:absolute;left:0;top:0;width:100%;height:60px;z-index:3}
.brand{position:absolute;left:87px;top:16px;display:flex;align-items:center;gap:8px;color:#fff;font-family:var(--cond);font-stretch:condensed;font-size:16px;letter-spacing:.5px}
.brand i{width:14px;height:14px;border-radius:50%;background:var(--blue);display:block}
.menu{position:absolute;right:100px;top:20px;display:flex;gap:30px;list-style:none;font-size:11px;color:#eef}
.menu li.active{color:var(--blue);border-bottom:1px solid var(--blue);padding-bottom:6px}
/* scroll marker */
.marker{position:absolute;width:68px;height:68px;border-radius:50%;background:rgba(255,255,255,.18);display:flex;align-items:center;justify-content:center;z-index:2}
.vline{position:absolute;width:1px;background:rgba(200,210,220,.8);z-index:2}
.vlabel{position:absolute;writing-mode:vertical-rl;font-size:9px;letter-spacing:2px;color:rgba(255,255,255,.85);font-style:italic;z-index:2}
/* intro */
.intro-box{position:absolute;left:0;top:396px;width:401px;height:211px;background:#fff;z-index:2}
.intro-box .kicker{position:absolute;left:45px;top:80px;font-family:var(--cond);font-stretch:condensed;font-size:29px;color:var(--ink);line-height:1}
.intro-box h1{position:absolute;left:45px;top:112px;font-family:var(--cond);font-stretch:condensed;font-weight:400;font-size:50px;color:var(--blue-head);line-height:1}
.intro-box .rule{position:absolute;left:45px;top:170px;width:52px;height:1px;background:var(--blue)}
.intro-copy{position:absolute;left:440px;top:478px;width:530px;font-size:12.4px;line-height:24px;font-weight:300}
.intro-copy p{margin-bottom:24px}
.intro-copy p.tight{margin-bottom:8px;line-height:20px}
.intro-copy .lead{font-family:var(--cond);font-stretch:condensed;font-size:19px;color:var(--ink);margin-bottom:28px;font-weight:400}
.link{font-family:var(--cond);font-stretch:condensed;font-size:13px;color:var(--blue-head);letter-spacing:.6px}
/* mission */
.mission-copy{position:absolute;left:37px;top:868px;width:310px;font-size:12.4px;line-height:24px;font-weight:300}
.mission-line{position:absolute;left:349px;top:892px;width:240px;height:1px;background:var(--blue);z-index:2}
.mission-title{position:absolute;left:592px;top:860px;font-family:var(--cond);font-stretch:condensed;font-size:48px;color:#fff;z-index:2}
/* features */
.feature{position:absolute;top:1218px;width:228px}
.feature svg{position:absolute;left:-40px;top:-64px}
.feature h3{font-family:var(--cond);font-stretch:condensed;font-weight:400;font-size:17px;color:var(--blue-head);line-height:20px;margin-bottom:12px;position:relative}
.feature p{font-size:10px;line-height:18px;color:#444;position:relative}
/* services */
.service{position:absolute;top:1690px;height:282px;text-align:center;color:#fff}
.service h2{font-family:var(--cond);font-stretch:condensed;font-weight:400;font-size:36px;margin-top:14px}
.service svg{margin-top:44px}
.service .link{color:#fff;display:inline-block;margin-top:38px;border-bottom:1px solid rgba(255,255,255,.6)}
/* history */
.history{position:absolute;left:0;top:2279px;width:100%;height:302px;background:var(--soft);text-align:center}
.history h2{font-family:var(--cond);font-stretch:condensed;font-weight:400;font-size:32px;color:var(--blue-head);margin-top:44px}
.history .sub{font-family:var(--cond);font-stretch:condensed;font-size:16px;color:var(--ink);margin-top:8px}
.year{position:absolute;left:474px;top:156px;width:62px;height:20px;background:var(--blue);color:#fff;font-size:10px;line-height:20px}
.history-card{position:absolute;left:524px;top:206px;width:370px;height:110px;background:#fff;text-align:left;padding:24px 22px;font-size:12.4px;line-height:24px;font-weight:300}
</style>
</head>
<body>
<div class="page">

  <header class="nav">
    <div class="brand"><i></i>BRISK</div>
    <ul class="menu">
      <li class="active">Home</li><li>About Us</li><li>Services</li><li>Portfolio</li><li>Contact</li>
    </ul>
  </header>

  <div class="photo" role="img" aria-label="Rower in a red scull on a harbour with boats behind" style="left:0;top:0;width:1002px;height:461px;background:linear-gradient(180deg,rgba(150,160,168,.9) 0%,rgba(190,196,200,.6) 22%,rgba(120,134,144,.6) 36%,rgba(70,88,100,.2) 55%,rgba(150,40,55,.55) 62%,rgba(60,70,80,.2) 72%),linear-gradient(180deg,#8d99a3 0%,#6f7f8c 30%,#3f5363 50%,#33434f 75%,#232d36 100%)"></div>

  <div class="marker" style="left:90px;top:137px"><svg width="14" height="14" viewBox="0 0 14 14"><path d="M7 2v9M3 7l4 4 4-4" stroke="#fff" stroke-width="1.4" fill="none"/></svg></div>
  <div class="vline" style="left:124px;top:205px;height:395px"></div>
  <div class="vlabel" style="left:126px;top:220px">WHAT IS BRISK</div>

  <section class="intro-box">
    <div class="kicker">WHAT IS</div>
    <h1>BRISK</h1>
    <div class="rule"></div>
  </section>

  <div class="intro-copy">
    <p>BRISK is about empowering your innate talent. We give our community of artists a platform to do good, to earn a living wage, and to make an impact. This collective allows our clients to work with some of the most talented people in the world to help elevate their message, connect in new ways, and grow.</p>
    <p class="tight">We are content architects, engineers, and artists. BRISK is not just for meeting today's challenge. We are your partner for success.</p>
    <p class="tight">BRISK is not just for meeting today's challenge.</p>
    <p class="lead">We are your partner for success</p>
    <span class="link">Read More &rarr;</span>
  </div>

  <div class="photo" role="img" aria-label="Team of crew members with camera rigs posing at an event" style="left:0;top:607px;width:401px;height:224px;background:linear-gradient(180deg,#7d8690 0%,#555b64 35%,#3a3d44 60%,#6b3438 80%,#2b2d32 100%)"></div>

  <div class="mission-copy">Many business and organizations are overwhelmed and struggle to deliver high quality content that speaks to their brand, connects with their customers, and produces results. Our TEAM helps our clients identify their story. We then guide and create beautiful content to communicate their story in variety of video formats.</div>
  <div class="photo" role="img" aria-label="Two smiling team leaders in suits seated indoors" style="left:401px;top:831px;width:601px;height:265px;background:linear-gradient(180deg,#2a2c30 0%,#3a3e45 40%,#4b5563 75%,#2d3440 100%)"></div>
  <div class="mission-line"></div>
  <div class="mission-title">Our Mission</div>

  <div class="feature" style="left:107px">
    <svg width="80" height="80" viewBox="0 0 80 80" fill="none" stroke="#e4e8ec" stroke-width="2"><path d="M20 10h40v18a20 20 0 0 1-40 0z"/><path d="M20 16H8v6a12 12 0 0 0 12 12M60 16h12v6a12 12 0 0 1-12 12M40 48v14M28 70h24"/></svg>
    <h3>A reputation for award winning content</h3>
    <p>With over 1000 videos produced in the last five years clients have complete confidence we deliver. The proof is in our product. High quality award winning storytelling and content. It's who we are.</p>
  </div>
  <div class="feature" style="left:386px">
    <svg width="80" height="80" viewBox="0 0 80 80" fill="none" stroke="#e4e8ec" stroke-width="2"><path d="M12 14h56v38H34l-14 12V52h-8z"/><path d="M24 28h32M24 38h22"/></svg>
    <h3>We listen</h3>
    <p>You may not know how to tell your story... but you know your brand, your goals, your assets, what makes your company awesome. We absorb all of that and create a plan and content unique to you, your business and your goals.</p>
  </div>
  <div class="feature" style="left:663px">
    <svg width="80" height="80" viewBox="0 0 80 80" fill="none" stroke="#e4e8ec" stroke-width="2"><circle cx="40" cy="38" r="28"/><ellipse cx="40" cy="38" rx="12" ry="28"/><path d="M12 38h56M16 24h48M16 52h48"/></svg>
    <h3>The experience matters</h3>
    <p>It is not enough just to make great content. We are committed to delivering are great experience. We meet our deadlines. We meet your expectations. We return your calls and emails. Our competitors are focused on the technicals. We are focused on the intangibles.</p>
  </div>

  <div class="photo" role="img" aria-label="City skyline lit up at night" style="left:0;top:1384px;width:1002px;height:306px;background:linear-gradient(180deg,#1d2440 0%,#253052 30%,#2b2f45 55%,#3b3336 78%,#2a2a30 100%)"></div>
  <div class="marker" style="left:467px;top:1390px"><svg width="14" height="14" viewBox="0 0 14 14"><path d="M7 2v9M3 7l4 4 4-4" stroke="#fff" stroke-width="1.4" fill="none"/></svg></div>
  <div class="vline" style="left:501px;top:1458px;height:214px"></div>
  <div class="vlabel" style="left:503px;top:1480px">Our Services</div>

  <section class="service" style="left:0;width:502px;background:var(--blue-deep)">
    <svg width="64" height="56" viewBox="0 0 64 56" fill="none" stroke="#dff2fb" stroke-width="2.4"><circle cx="14" cy="10" r="7"/><circle cx="34" cy="10" r="7"/><rect x="6" y="24" width="36" height="24"/><path d="M42 32l14-8v24l-14-8"/></svg>
    <h2>Video Services</h2>
    <span class="link">Learn More &rarr;</span>
  </section>
  <section class="service" style="left:502px;width:500px;background:var(--blue)">
    <svg width="64" height="56" viewBox="0 0 64 56" fill="none" stroke="#dff2fb" stroke-width="2.4"><path d="M4 14h14l6-8h16l6 8h14v36H4z"/><circle cx="32" cy="31" r="11"/><circle cx="32" cy="31" r="5"/></svg>
    <h2>Photography Services</h2>
    <span class="link">Learn More &rarr;</span>
  </section>

  <div class="photo" role="img" aria-label="Black and white portrait of a couple holding an award statuette" style="left:0;top:1972px;width:1002px;height:307px;background:linear-gradient(180deg,#2a2a2a 0%,#4a4a4a 35%,#5e5e5e 65%,#3a3a3a 100%)"></div>
  <div class="marker" style="left:467px;top:1982px"><svg width="14" height="14" viewBox="0 0 14 14"><path d="M7 2v9M3 7l4 4 4-4" stroke="#fff" stroke-width="1.4" fill="none"/></svg></div>
  <div class="vline" style="left:501px;top:2050px;height:531px"></div>
  <div class="vlabel" style="left:503px;top:2110px">Our History</div>

  <section class="history">
    <h2>OUR HISTORY</h2>
    <p class="sub">BRISK is the product of more than a decade of forward thinking, evolution, transformation.</p>
    <div class="year">2008</div>
    <div class="photo" role="img" aria-label="Mountain landscape under a blue sky with clouds" style="left:109px;top:184px;width:369px;height:130px;background:linear-gradient(180deg,#3f78b8 0%,#7fa6cf 45%,#4f6b70 75%,#2f4536 100%)"></div>
    <div class="history-card">We got our start in 2008 by Marco Lenhill who envisioned turning a photography hobby into a small business. Marco Lenhill Photography serviced</div>
  </section>

</div>
</body>
</html>
```